Evaporative Air Conditioning Summer Service

Would like to design a flyer to send out in an email to existing clients to promote a Pre-summer service for Evaporative Air Conditioners
Cost will be $110.00 inc gst
Tasks included in service are
- Inspection and clean of pads
- Inspection and check float valve, water pump, fan, motor, bearings, drain
- Clean basin
- Supply of bacterial tablet
- Inspect overall condition of unit
- Any repairs if required will be quoted
Please see files attached of a previous very basic flyer I have used for installation and replacement unit costs. This has current contact information
Have also uploaded company logo for use.
Thanks

```html
<!DOCTYPE html>
<html lang="en">
<head>
<meta charset="utf-8">
<title>Pinnacle Gas &amp; Plumbing – Evaporative Summer Service</title>
<link rel="stylesheet" href="https://fonts.googleapis.com/css2?family=Montserrat:wght@700;800;900&family=Poppins:wght@400;600;700&display=swap">
<style>
  :root {
    --stage: #d5d8d3;
    --ink: #000000;
    --brand-blue: #2a55d0;
    --phone-blue: #2348c4;
    --heading-yellow: #ffd21a;
    --list-orange: #f7a21b;
    --price-red: #e8141c;
    --white: #ffffff;
    --badge-grey-light: #c4c7cb;
    --badge-grey-dark: #46494e;
    --flame-yellow: #ffd21a;
    --flame-orange: #f2682a;
    --unit-grey: #4f5457;
    --roof-grey: #2c2f31;
    --pad-copper: #b8702c;
  }
  * { box-sizing: border-box; margin: 0; padding: 0; }
  html, body {
    width: 1200px; height: 800px; overflow: hidden;
    background: var(--stage);
  }
  .flyer {
    position: absolute; left: 306px; top: 20px;
    width: 588px; height: 760px;
    background: var(--ink); overflow: hidden;
    font-family: "Poppins", sans-serif; color: var(--white);
  }
  .brand {
    position: absolute; left: 56px; top: 80px;
    display: flex; align-items: center; gap: 30px;
  }
  .brand-dot {
    width: 80px; height: 80px; border-radius: 50%;
    background: var(--brand-blue);
  }
  .brand-name {
    font-family: "Montserrat", sans-serif; font-weight: 800;
    color: var(--brand-blue); line-height: 1;
  }
  .brand-name .word { display: block; font-size: 56px; letter-spacing: 1px; }
  .brand-name .trade { display: block; font-size: 19px; letter-spacing: 2px; margin-top: 6px; text-align: center; }
  .unit-photo {
    position: absolute; left: 0; top: 184px; width: 588px; height: 300px;
    background:
      radial-gradient(ellipse 34% 30% at 57% 38%, var(--pad-copper) 0%, rgba(184,112,44,.55) 45%, rgba(184,112,44,0) 100%),
      radial-gradient(ellipse 46% 48% at 57% 42%, #6a6f72 0%, var(--unit-grey) 55%, rgba(79,84,87,0) 100%),
      linear-gradient(180deg, #141516 0%, var(--roof-grey) 35%, #1e2022 75%, #000 100%);
  }
  .price-badge {
    position: absolute; left: 424px; top: 360px;
    width: 150px; height: 150px; border-radius: 50%;
    border: 8px solid var(--white);
    background: radial-gradient(circle at 40% 35%, var(--badge-grey-light), var(--badge-grey-dark));
    display: flex; flex-direction: column; align-items: center; justify-content: center;
    text-align: center;
  }
  .price-badge .lead { font-size: 13px; letter-spacing: .5px; }
  .price-badge .amount {
    font-family: "Montserrat", sans-serif; font-weight: 900; line-height: 1;
    display: flex; align-items: flex-start;
  }
  .price-badge .currency { font-size: 20px; margin-top: 18px; }
  .price-badge .value { font-size: 44px; color: var(--price-red); }
  .price-badge .cents { font-size: 14px; margin-top: 6px; }
  .price-badge .tax { font-size: 11px; }
  .repairs-note {
    position: absolute; left: 16px; top: 536px; width: 132px; height: 112px;
    transform: rotate(-8deg);
    display: flex; flex-direction: column; align-items: center; justify-content: center;
    text-align: center; color: var(--price-red);
  }
  .repairs-note .flash {
    position: absolute; inset: 0; border-radius: 14px;
    background: linear-gradient(160deg, var(--flame-yellow) 0%, var(--flame-orange) 100%);
  }
  .repairs-note p { position: relative; font-weight: 700; font-size: 10.5px; line-height: 1.15; }
  .repairs-note .big { font-family: "Montserrat", sans-serif; font-weight: 900; font-size: 26px; line-height: 1; }
  .service-tasks {
    position: absolute; left: 164px; top: 534px; width: 400px;
    transform: rotate(-2deg); transform-origin: left top;
  }
  .service-tasks h2 {
    font-family: "Montserrat", sans-serif; font-weight: 800;
    font-size: 22.5px; color: var(--heading-yellow); white-space: nowrap;
  }
  .service-tasks ul { list-style: none; margin-top: 2px; }
  .service-tasks li {
    font-weight: 700; font-size: 13px; line-height: 16.5px; color: var(--list-orange);
    padding-left: 12px; text-indent: -12px;
  }
  .service-tasks li::before { content: "- "; }
  .phone {
    position: absolute; left: 0; width: 588px; top: 656px; text-align: center;
    font-family: "Montserrat", sans-serif; font-weight: 900; line-height: 1;
    font-size: 60px; color: var(--phone-blue); letter-spacing: 1px;
  }
  .email {
    position: absolute; left: 0; width: 588px; top: 730px; text-align: center;
    font-weight: 600; font-size: 17px; line-height: 1; letter-spacing: 3.6px;
  }
</style>
</head>
<body>
  <main class="flyer">
    <div class="unit-photo" role="img" aria-label="Photo of a grey evaporative air conditioning unit with copper cooling pads, mounted on a corrugated metal roof"></div>

    <header class="brand">
      <span class="brand-dot"></span>
      <h1 class="brand-name">
        <span class="word">PINNACLE</span>
        <span class="trade">GAS &amp; PLUMBING</span>
      </h1>
    </header>

    <div class="price-badge">
      <span class="lead">Cost will be</span>
      <span class="amount"><span class="currency">$</span><span class="value">110</span><span class="cents">/00</span></span>
      <span class="tax">inc gst</span>
    </div>

    <section class="service-tasks">
      <h2>Tasks included in service are</h2>
      <ul>
        <li>Inspection and clean of pads</li>
        <li>Inspection and check float valve, water pump, fan, motor, bearings, drain</li>
        <li>Clean basin</li>
        <li>Supply of bacterial tablet</li>
        <li>Inspect overall condition of unit</li>
      </ul>
    </section>

    <aside class="repairs-note">
      <span class="flash" role="img" aria-label="Flame coloured splash"></span>
      <p>Any repairs if<br>required will be</p>
      <p class="big">quoted</p>
    </aside>

    <p class="phone">400 555 017</p>
    <p class="email">admin@pinnaclegasandplumbing.com.au</p>
  </main>
</body>
</html>
```